dentist office tri-fold for root canal specialist

design a tri fold brochure to give to patients talking about the office and the services
Talk about doctors and their bios
services: root canal , retreatments, endodontic surgery, trauma, cracked teeth
Technology: CBCT, microscopes, lasers, clear pulse advanced
I will provide all the technical info. willing to hire a writer if needed. Attached a picture of our logo as a reference of our colors. Can attach older versions of brochure if requested. Looking for a very professional tri fold that will be used to market the practice to patients and other doctors.
Rough idea: TRIFOLD
Front Cover:
Welcome to The Halvern Team
Thank you for allowing us to care for your endodontic needs. We look forward to serving you.
We at The Halvern Team have dedicated our professional lives to improving the comfort and dental health of those in our care.
Inner Right:
Pics of Docs
Welcome – On behalf of our staff, we welcome you to our office.
We are pleased that you have selected our team of professionals to care for your endodontic needs. We want you to know that we are committed to providing you, our patient with the highest quality endodontic care in the most gentle, efficient, and caring manner possible. We pride ourselves on offering our expertise along with the best patient care with the most up to date technologies to better ensure your oral health.
For your convenience, please visit us online at www.thehalvernteam.com for directions to our offices, pre and post-operative instructions, general information on our Endodontists and much more. We are here for you and our doctors are on call 24 hours a day, 7 days a week.
We are looking forward providing you a most relaxed and pleasant vist possible. Thank you again for choosing The Halvern Team.
Inner Middle:
What is a Root Canal?
A root canal (endodontic treatment) is one of the most common dental procedures performed, with more than 14 million performed every year. This simple treatment can save your natural teeth and prevent the need of dental implants or bridges.
At the center of your tooth is pulp. The pulp is a collection of blood vessels, nerves and lymphatics, which help to form the tooth during the stages of tooth development.
I’ve already had a root canal, why do I need another procedure?
Retreatment - A second chance to save your tooth
With proper care, most teeth which have had endodontic (root canal) treatment can last as long as other natural teeth.
However, in a few cases, a tooth that has received endodontic treatment fails to heal completely. And occasionally, a tooth becomes painful or diseased months or even years after previously successful endodontic treatment.
If your tooth has failed to heal or has developed new problems, you have a second chance. Another endodontic procedure, called retreatment, may be able to save your tooth.
Retreated teeth can function well for years, even for a lifetime. It's always best to save the tooth if your endodontist believes retreatment is the best option for you.
Advances in technology are constantly changing the way root canal treatment is performed, so your endodontist may even be able to use a new technique that was not available when you had your first procedure.
Of course, there are no guarantees with any dental or medical procedure. Your endodontist will discuss your options and the chances of success before beginning retreatment.
What is an Apicoectomy?
In this procedure, the endodontist opens the gum tissue near the tooth to see the underlying bone and to remove any inflamed or infected tissue. The very end of the root is also removed or resected.
Inner Right:
Patient Care: Needing a root canal is often a surprise and sometimes an emergency. We at The Halvern Team make certain that every patient receives prompt emergency care at any time.
We understand how uneasy some patients may feel about dental visits and how we can make a difference in providing a relaxing, positive experience. Our doctors are trained in different levels of sedation dentistry from Nitrous Oxide to Conscious Sedation.
Our entire team is dedicated to providing you with excellent, personalized care and service to make your visit as comfortable and pleasant as possible. You will enjoy our relaxing treatment rooms, complete with plumacore coverings, televisions and Tunelets for your use during treatment and blankets to keep you warm if you’re cold.
Technical Equipment: The Halvern Team prides itself in utilizing the most advanced techniques and state-of-the-art equipment including digital radiography, fiber optic illumination, ultrasonic equipment, and operating microscopes, which help the doctor see microscopic details inside a tooth during micro-surgical and non-surgical procedures.
Expertise: The Halvern Team is staffed by doctors who are responsive to your concerns and alert to your experience during treatment. All of our doctors are endodontists, which means they are specialists who have completed 2-3 years of advanced training in addition to dental school. We are all specialist members of the Continental Society of Pulp Specialists (CSPS). All our endodontists continue their education and training through professional associations, seminars, study groups, and teaching both at Pellmoor and Dorrin Universities.

```html
<!DOCTYPE html>
<html lang="en">
<head>
<meta charset="utf-8">
<title>The Halvern Team – Tri-fold Brochure</title>
<link href="https://fonts.googleapis.com/css2?family=Nunito+Sans:ital,wght@0,300;0,400;0,600;0,700;0,800;1,700&family=Tinos&family=Yellowtail&display=swap" rel="stylesheet">
<style>
:root{
  --stage:#a9aaaf;
  --paper:#ffffff;
  --lilac:#6e76a6;
  --lilac-soft:#8a90b8;
  --navy:#2e3a5e;
  --ink:#333640;
  --mist:#eceef2;
  --photo-cool:#d9dde6;
  --photo-warm:#e6dcd6;
}
*{margin:0;padding:0;box-sizing:border-box}
html,body{width:757px;height:1200px;overflow:hidden}
body{background:var(--stage);font-family:"Nunito Sans",sans-serif;color:var(--ink);position:relative}
.spread{position:absolute;left:82px;width:593px;height:459px;background:var(--paper);overflow:hidden}
.spread--outside{top:96px}
.spread--inside{top:614px}
.spread svg.shapes{position:absolute;inset:0}
.abs{position:absolute}

/* outside */
.cover-intro{left:26px;top:322px;width:150px;color:#fff;font-weight:300;font-size:9.6px;line-height:12.3px}
.cover-rule{left:26px;top:410px;width:23px;height:1.5px;background:#fff}
.cover-url{left:26px;top:419px;color:#fff;font-size:6px;letter-spacing:1.6px}
.thanks{left:225px;top:180px;width:140px;color:var(--navy);font-weight:800;font-size:13.5px;line-height:17px}
.forward{left:225px;top:262px;width:140px;color:var(--lilac);font-weight:400;font-size:13px;line-height:17px;letter-spacing:.6px}
.brand{color:var(--navy);font-weight:400;letter-spacing:.4px}
.brand--back{left:222px;top:342px;font-size:12px}
.brand--cover{left:455px;top:40px;font-size:12px}
.address{top:373px;width:80px;font-size:7px;line-height:9.2px;color:var(--ink);padding-left:8px}
.address--one{left:222px}
.address--two{left:302px}
.address svg,.phone svg{position:absolute;left:0;top:1px}
.phone{top:409px;font-size:8px;font-weight:700;color:var(--ink);padding-left:8px}
.phone--one{left:222px}
.phone--two{left:302px}
.url-pill{left:229px;top:430px;width:138px;height:12px;border:1px solid var(--ink);border-radius:6px;font-size:6px;letter-spacing:1.6px;text-align:center;line-height:10px}
.welcome-cover{left:416px;top:244px;width:100px;color:var(--navy);font-size:14.8px;line-height:18.2px}
.welcome-cover b{font-weight:800}

/* inside */
.welcome-script{left:32px;top:183px;font-family:"Yellowtail",cursive;color:#fff;font-size:34px}
.welcome-sub{left:33px;top:225px;width:150px;color:#fff;font-size:8.6px;line-height:11px;font-weight:300}
.welcome-body{left:32px;top:258px;width:147px;color:#fff;font-size:6.1px;line-height:8.1px;text-align:justify}
.welcome-body p{margin-bottom:8px}
.section-title{left:198px;top:16px;width:199px;text-align:center;color:#fff;font-weight:800;font-size:12px}
.rc-body{left:221px;top:71px;width:155px;font-size:6.6px;line-height:8.5px;text-align:justify}
.rc-body p{margin-bottom:4px}
.question{left:214px;top:185px;width:163px;height:30px;border-radius:15px;background:var(--lilac);color:#fff;font-weight:600;font-size:7.4px;line-height:9.6px;text-align:center;padding-top:5px}
.retreat-head{left:214px;top:224px;width:163px;text-align:center;font-style:italic;font-weight:700;font-size:7.6px;line-height:10px;color:var(--ink)}
.retreat-body{left:218px;top:254px;width:158px;font-size:4.85px;line-height:6.3px;text-align:justify}
.retreat-body p{margin-bottom:2.4px}
.care-title{left:412px;top:88px;font-family:"Tinos",serif;color:var(--lilac);font-size:20px}
.care-rule{left:412px;top:122px;width:36px;height:2px;background:var(--lilac)}
.care-body{left:412px;top:134px;width:156px;font-size:6.2px;line-height:8.1px;text-align:justify}
.care-body p{margin-bottom:2.5px}
</style>
</head>
<body>

<!-- OUTSIDE SPREAD -->
<section class="spread spread--outside">
  <svg class="shapes" width="593" height="459" viewBox="0 0 593 459">
    <defs>
      <linearGradient id="photoTone" x1="0" y1="0" x2="1" y2="1">
        <stop offset="0" stop-color="#e9ecef"/>
        <stop offset=".6" stop-color="var(--photo-warm)"/>
        <stop offset="1" stop-color="var(--photo-cool)"/>
      </linearGradient>
      <linearGradient id="familyTone" x1="0" y1="0" x2="1" y2="1">
        <stop offset="0" stop-color="#e7ddd4"/>
        <stop offset="1" stop-color="#9fb3cf"/>
      </linearGradient>
      <linearGradient id="lilacTone" x1="0" y1="0" x2="1" y2="0">
        <stop offset="0" stop-color="#7a80ae"/>
        <stop offset="1" stop-color="#6a72a2"/>
      </linearGradient>
    </defs>
    <rect x="397" y="0" width="196" height="459" fill="var(--mist)"/>
    <path d="M0,0 H398 V148 Q330,150 245,162 Q90,195 0,290 Z" fill="url(#photoTone)" role="img" aria-label="Photo of a smiling patient in a bright dental treatment room"/>
    <path d="M0,300 Q80,215 198,190 V198 Q75,225 0,318 Z" fill="var(--navy)"/>
    <path d="M0,324 Q70,240 198,203 V459 H0 Z" fill="url(#lilacTone)"/>
    <path d="M349,0 Q420,95 593,118 V124 Q415,108 343,0 Z" fill="#6a7496"/>
    <path d="M0,305 Q0,180 0,305" fill="none"/>
    <rect x="398" y="292" width="195" height="167" fill="url(#familyTone)" role="img" aria-label="Photo of a smiling family with two children riding piggyback"/>
  </svg>

  <p class="abs cover-intro">We at The Halvern Team have dedicated our professional lives to improving the comfort and dental health of those in our care.</p>
  <div class="abs cover-rule"></div>
  <p class="abs cover-url">www.thehalvernteam.com</p>

  <h2 class="abs thanks">Thank you for allowing us to care for your endodontic needs.</h2>
  <p class="abs forward">We look forward to serving you.</p>
  <p class="abs brand brand--back">The Halvern Team</p>

  <p class="abs address address--one">
    <svg width="6" height="8" viewBox="0 0 6 8"><path d="M3,0 A3,3 0 0 1 6,3 C6,5 3,8 3,8 C3,8 0,5 0,3 A3,3 0 0 1 3,0 Z" fill="var(--lilac)"/><circle cx="3" cy="3" r="1.1" fill="#fff"/></svg>
    82 ALDER ST,<br>BROOKHAVEN,<br>MA 01790</p>
  <p class="abs address address--two">
    <svg width="6" height="8" viewBox="0 0 6 8"><path d="M3,0 A3,3 0 0 1 6,3 C6,5 3,8 3,8 C3,8 0,5 0,3 A3,3 0 0 1 3,0 Z" fill="var(--lilac)"/><circle cx="3" cy="3" r="1.1" fill="#fff"/></svg>
    27 WEXLEY ST,<br>EASTON FALLS,<br>MA 01764</p>
  <p class="abs phone phone--one">
    <svg width="5" height="8" viewBox="0 0 5 8"><path d="M1.5,0 L0.5,0.6 Q-0.5,4 1.8,7.6 L3,7 L2.2,5.2 L1.5,5.3 Q0.9,4 1.3,2.6 L2,2.4 Z" fill="var(--lilac)"/></svg>
    555-014-2731</p>
  <p class="abs phone phone--two">
    <svg width="5" height="8" viewBox="0 0 5 8"><path d="M1.5,0 L0.5,0.6 Q-0.5,4 1.8,7.6 L3,7 L2.2,5.2 L1.5,5.3 Q0.9,4 1.3,2.6 L2,2.4 Z" fill="var(--lilac)"/></svg>
    555-019-6482</p>
  <p class="abs url-pill">www.thehalvernteam.com</p>

  <p class="abs brand brand--cover">The Halvern Team</p>
  <h1 class="abs welcome-cover"><b>Welcome</b><br>to The Halvern Team</h1>
</section>

<!-- INSIDE SPREAD -->
<section class="spread spread--inside">
  <svg class="shapes" width="593" height="459" viewBox="0 0 593 459">
    <defs>
      <linearGradient id="teamTone" x1="0" y1="0" x2="1" y2="0">
        <stop offset="0" stop-color="#e8e9ee"/>
        <stop offset="1" stop-color="#d8dbe4"/>
      </linearGradient>
      <linearGradient id="chairTone" x1="0" y1="0" x2="1" y2="1">
        <stop offset="0" stop-color="#9fb4d4"/>
        <stop offset=".5" stop-color="#e4e7ee"/>
        <stop offset="1" stop-color="#5577b8"/>
      </linearGradient>
      <linearGradient id="panelLilac" x1="0" y1="0" x2="1" y2="0">
        <stop offset="0" stop-color="#7a80ae"/>
        <stop offset="1" stop-color="#6a72a2"/>
      </linearGradient>
    </defs>
    <rect x="0" y="0" width="198" height="459" fill="url(#panelLilac)"/>
    <path d="M0,0 H198 V52 Q90,58 0,108 Z" fill="url(#teamTone)" role="img" aria-label="Group photo of six doctors in white coats"/>
    <path d="M0,108 Q90,58 198,52 V62 Q70,88 0,205 Z" fill="var(--navy)"/>
    <path d="M0,212 Q70,95 198,66 V70 Q75,100 0,222 Z" fill="#fff"/>
    <rect x="198" y="0" width="199" height="50" fill="var(--navy)"/>
    <path d="M198,50 H397 V47 Q290,45 198,60 Z" fill="var(--navy)"/>
    <path d="M198,62 Q300,44 420,48 Q500,52 593,118 V121 Q500,60 420,52 Q300,49 198,64 Z" fill="#8a93b4"/>
    <path d="M397,0 H593 V112 Q520,75 440,78 Q418,80 397,84 Z" fill="url(#chairTone)" role="img" aria-label="Photo of a smiling young patient in a dental chair viewing an x-ray on a tablet"/>
  </svg>

  <h2 class="abs welcome-script">Welcome</h2>
  <p class="abs welcome-sub">On behalf of our staff,<br>we welcome you to our office.</p>
  <div class="abs welcome-body">
    <p>We are pleased that you have selected our team of professionals to care for your endodontic needs. We want you to know that we are committed to providing you, our patient with the highest quality endodontic care in the most gentle, efficient, and caring manner possible. We pride ourselves on offering our expertise along with the best patient care with the most up to date technologies to better ensure your oral health.</p>
    <p>For your convenience, please visit us online at www.thehalvernteam.com for directions to our offices, pre and post-operative instructions, general information on our Endodontists and much more. We are here for you and our doctors are on call 24 hours a day, 7 days a week.</p>
    <p>We are looking forward providing you a most relaxed and pleasant vist possible. Thank you again for choosing The Halvern Team.</p>
  </div>

  <h2 class="abs section-title">What is a Root Canal?</h2>
  <div class="abs rc-body">
    <p>A root canal (endodontic treatment) is one of the most common dental procedures performed, with more than 14 million performed every year. This simple treatment can save your natural teeth and prevent the need of dental implants or bridges.</p>
    <p>At the center of your tooth is pulp. The pulp is a collection of blood vessels, nerves and lymphatics, which help to form the tooth during the stages of tooth development.</p>
  </div>
  <p class="abs question">I’ve already had a root canal,<br>why do I need another procedure?</p>
  <h3 class="abs retreat-head">Retreatment - A second chance to<br>save your tooth</h3>
  <div class="abs retreat-body">
    <p>With proper care, most teeth which have had endodontic (root canal) treatment can last as long as other natural teeth.</p>
    <p>However, in a few cases, a tooth that has received endodontic treatment fails to heal completely. And occasionally, a tooth becomes painful or diseased months or even years after previously successful endodontic treatment.</p>
    <p>If your tooth has failed to heal or has developed new problems, you have a second chance. Another endodontic procedure, called retreatment, may be able to save your tooth.</p>
    <p>Retreated teeth can function well for years, even for a lifetime. It's always best to save the tooth if your endodontist believes retreatment is the best option for you.</p>
    <p>Advances in technology are constantly changing the way root canal treatment is performed, so your endodontist may even be able to use a new technique that was not available when you had your first procedure.</p>
    <p>Of course, there are no guarantees with any dental or medical procedure. Your endodontist will discuss your options and the chances of success before beginning retreatment.</p>
    <p>What is an Apicoectomy?</p>
    <p>In this procedure, the endodontist opens the gum tissue near the tooth to see the underlying bone and to remove any inflamed or infected tissue. The very end of the root is also removed or resected.</p>
  </div>

  <h2 class="abs care-title">Patient Care</h2>
  <div class="abs care-rule"></div>
  <div class="abs care-body">
    <p>Needing a root canal is often a surprise and sometimes an emergency. We at The Halvern Team make certain that every patient receives prompt emergency care at any time.</p>
    <p>We understand how uneasy some patients may feel about dental visits and how we can make a difference in providing a relaxing, positive experience. Our doctors are trained in different levels of sedation dentistry from Nitrous Oxide to Conscious Sedation.</p>
    <p>Our entire team is dedicated to providing you with excellent, personalized care and service to make your visit as comfortable and pleasant as possible. You will enjoy our relaxing treatment rooms, complete with plumacore coverings, televisions and Tunelets for your use during treatment and blankets to keep you warm if you’re cold.</p>
    <p>Technical Equipment: The Halvern Team prides itself in utilizing the most advanced techniques and state-of-the-art equipment including digital radiography, fiber optic illumination, ultrasonic equipment, and operating microscopes, which help the doctor see microscopic details inside a tooth during micro-surgical and non-surgical procedures.</p>
    <p>Expertise: The Halvern Team is staffed by doctors who are responsive to your concerns and alert to your experience during treatment. All of our doctors are endodontists, which means they are specialists who have completed 2-3 years of advanced training in addition to dental school. We are all specialist members of the Continental Society of Pulp Specialists (CSPS). All our endodontists continue their education and training through professional associations, seminars, study groups, and teaching both at Pellmoor and Dorrin Universities.</p>
  </div>
</section>

</body>
</html>
```